Poster for Billard- & Sportsbar: "Specials"

Hi,
I Need a Poster for my Billard- & Sportsbar, which Shows our weekly Specials.
The size should be DinA0 (84 x 118.8 cm). Please notice the print instructions attached.

Text Information for the Poster:

"Wochenhighlights

Dienstag: Flatrate-Billard
Für nur 5€ (7€) pro Person den ganzen Abend Pool-Billard (Snooker)spielen

Mittwoch: Studenten-Nacht
Studenten & Auszubildende spielen Pool-Billard für nur 4,50€ die Stunde

Donnerstag: Snooker-Donnerstag
Donnerstags kostet der Snooker Tisch gerade mal 5€ die Stunde

Freitag: Kesselgold-Special
6 Talhof Kesselgold-Pils für nur 11,99€

Samstag: Schau dein Wunschsspiel
Reserviere die Private Lounge und schaue das Staffelrunde-Spiel deiner Wahl. Reservierungsgebühr: 10€, ab 6 Personen kostenlos.
(Gilt auch für EP, VKT-Pokal & Englische Wochen)

Sonntag: Play for Free
Wer vor 18:00 Uhr mit dem Spielen beginnt, spielt den ganzen Abend umsonst!"

You can choose the Colors free. If you use Pictures, take care that they are free or send me the link where they can get bought.

I have uploaded the logo of my bar. You can use it in the poster, but please not too big.

You can maybe use the Colors of the logo as main Colors. But it is not a must.

If you have questions, just contact me!

Thank you in advance!

Jorik

A short update: Please mind, that it is the most important Thing, that the customers can read the Special offers! Thank you

```html
<!DOCTYPE html>
<html lang="de">
<head>
<meta charset="utf-8">
<title>Wochenhighlights – Bandenbar</title>
<link rel="stylesheet" href="https://fonts.googleapis.com/css2?family=Open+Sans:wght@400;600;700&family=Open+Sans+Condensed:wght@700&family=Kalam:wght@300&display=swap">
<style>
  :root {
    --teal: #5cc4bf;
    --ink: #3f3f3f;
    --paper: #f1f1f1;
    --paper-light: #f7f7f7;
    --paper-shade: #e4e4e4;
    --table-frame: #3a3a3a;
    --table-cloth: #8e8e8e;
    --white: #ffffff;
    --hand: #2b2b2b;
  }
  * { margin: 0; padding: 0; box-sizing: border-box; }
  html, body { width: 849px; height: 1200px; overflow: hidden; background: var(--paper); }
  .poster {
    position: relative;
    width: 849px;
    height: 1200px;
    overflow: hidden;
    background: var(--paper);
    color: var(--ink);
    font-family: "Open Sans", sans-serif;
  }
  .backdrop { position: absolute; inset: 0; }

  .headline {
    position: absolute;
    left: 14px;
    top: 48px;
    font-family: "Open Sans", sans-serif;
    font-weight: 600;
    font-size: 80px;
    letter-spacing: -1px;
    line-height: 1;
    text-shadow: 4px 4px 0 #c9c9c9;
    white-space: nowrap;
  }
  .headline .accent { color: var(--teal); font-family: "Open Sans Condensed", sans-serif; font-weight: 700; }
  .headline .rest { color: var(--ink); }

  .dash-line { position: absolute; border: 0 dashed #555; }
  .dash-top { left: 0; top: 141px; width: 766px; border-top-width: 1.5px; }
  .dash-right { left: 764px; top: 141px; height: 340px; border-left-width: 1.5px; }
  .dash-bottom { left: 0; top: 578px; width: 722px; border-top-width: 1.5px; }
  .dash-side { left: 722px; top: 578px; height: 300px; border-left-width: 1.5px; }

  .ball-cue {
    position: absolute;
    left: 0; top: 215px;
    width: 120px; height: 140px;
    border-radius: 0 60px 60px 0;
    background: linear-gradient(135deg, #6a6a6a, #3a3a3a);
    opacity: .8;
  }
  .table-corner {
    position: absolute;
    left: 712px; top: 482px;
    width: 150px; height: 395px;
    background: linear-gradient(180deg, var(--table-frame) 0 5%, var(--table-cloth) 5% 95%, var(--table-frame) 95%);
    border-left: 18px solid var(--table-frame);
    border-radius: 14px 0 0 10px;
    transform: rotate(3deg);
    transform-origin: top left;
  }

  .special { position: absolute; }
  .special .day {
    font-family: "Open Sans Condensed", sans-serif;
    font-weight: 700;
    font-size: 24px;
    color: var(--ink);
  }
  .special .name {
    font-family: "Open Sans", sans-serif;
    font-weight: 400;
    font-size: 24px;
    color: var(--teal);
  }
  .special .offer {
    font-family: "Kalam", cursive;
    font-weight: 300;
    font-size: 28px;
    line-height: 38px;
    margin: 2px 0 0 26px;
    color: var(--hand);
    white-space: nowrap;
  }
  .week-tuesday { left: 117px; top: 166px; width: 640px; }
  .week-wednesday { left: 117px; top: 306px; width: 640px; }
  .week-thursday { left: 117px; top: 438px; width: 640px; }

  .weekend-panel {
    position: absolute;
    left: 0; top: 592px;
    width: 722px; height: 700px;
    background: var(--teal);
    transform: rotate(3deg);
    transform-origin: top left;
  }
  .weekend-title {
    position: absolute;
    left: 78px; top: 598px;
    font-family: "Open Sans Condensed", sans-serif;
    font-weight: 700;
    font-size: 60px;
    color: var(--white);
    opacity: .92;
  }
  .weekend .special .name { color: var(--white); }
  .week-friday { left: 64px; top: 690px; width: 620px; transform: rotate(1deg); transform-origin: left top; }
  .week-friday .offer { margin-left: 22px; }
  .week-saturday { left: 58px; top: 782px; width: 620px; transform: rotate(4deg); transform-origin: left top; }
  .week-saturday .offer { margin-left: 22px; }
  .week-sunday { left: 38px; top: 1040px; width: 640px; transform: rotate(2deg); transform-origin: left top; }
  .week-sunday .offer { margin-left: 22px; }

  .brand {
    position: absolute;
    left: 742px; top: 1162px;
    font-family: "Open Sans", sans-serif;
    font-weight: 700;
    font-size: 17px;
    color: var(--ink);
    white-space: nowrap;
  }
</style>
</head>
<body>
<main class="poster">
  <svg class="backdrop" width="849" height="1200" viewBox="0 0 849 1200" aria-hidden="true">
    <polygon points="190,0 849,0 849,560" fill="var(--paper-light)"/>
    <polygon points="0,250 0,575 360,575" fill="var(--paper-shade)"/>
    <polygon points="730,860 849,760 849,1200 730,1200" fill="#e9e9e9"/>
  </svg>

  <h1 class="headline"><span class="accent">WOCHEN</span><span class="rest">HIGHLIGHTS</span></h1>

  <div class="dash-line dash-top"></div>
  <div class="dash-line dash-right"></div>
  <div class="dash-line dash-bottom"></div>

  <div class="ball-cue" role="img" aria-label="Billardkugel mit Queue"></div>

  <section class="week">
    <article class="special week-tuesday">
      <h2><span class="day">Dienstag</span> <span class="name">Flatrate-Billard</span></h2>
      <p class="offer">Für nur 5€ (7€) pro Person den ganzen Abend<br>Pool-Billard (Snooker)spielen</p>
    </article>
    <article class="special week-wednesday">
      <h2><span class="day">Mittwoch</span> <span class="name">Studenten-Nacht</span></h2>
      <p class="offer">Studenten &amp; Auszubildende spielen Pool-Billard<br>für nur 4,50€ die Stunde</p>
    </article>
    <article class="special week-thursday">
      <h2><span class="day">Donnerstag</span> <span class="name">Snooker-Donnerstag</span></h2>
      <p class="offer">Donnerstags kostet der Snooker Tisch gerade<br>mal 5€ die Stunde</p>
    </article>
  </section>

  <div class="table-corner" role="img" aria-label="Ecke eines Billardtisches von oben"></div>

  <section class="weekend">
    <div class="weekend-panel"></div>
    <div class="dash-line dash-side"></div>
    <h2 class="weekend-title">Wochenende</h2>
    <article class="special week-friday">
      <h3><span class="day">Freitag</span> <span class="name">Kesselgold-Special</span></h3>
      <p class="offer">6 Talhof Kesselgold-Pils für nur 11,99€</p>
    </article>
    <article class="special week-saturday">
      <h3><span class="day">Samstag</span> <span class="name">Schau dein Wunschsspiel</span></h3>
      <p class="offer">Reserviere die Private Lounge und schaue das<br>Staffelrunde-Spiel deiner Wahl. Reservierungs-<br>gebühr: 10€, ab 6 Personen kostenlos.<br>(Gilt auch für EP, VKT-Pokal &amp; Englische<br>Wochen)</p>
    </article>
    <article class="special week-sunday">
      <h3><span class="day">Sonntag</span> <span class="name">Play for Free</span></h3>
      <p class="offer">Wer vor 18:00 Uhr mit dem Spielen beginnt, spielt<br>den ganzen Abend</p>
    </article>
  </section>

  <div class="brand">Bandenbar</div>
</main>
</body>
</html>
```